Need Poster Design for Indie Family Film

We need a poster for a indie family film and would like to see designs that should be elegant, bold and playful.

Willowmere follows the parallel stories of three Singaporeans dealing with familial love and loss: a young girl copes with her mother’s death by living in an imaginary world, a father struggles to reconcile with his estranged daughter before her wedding and a woman fails to convince her family of her desire to become a singer. Staring Marisol Teng, Delia Rahn with veterans Noriza Latef, Rashid Tembo and Gavin Lu and Trevor Pak

Target Market(s)

7-14 and Parents

Number of Pages Required

3 page

Font styles to use
Serif

Requirements
Must have
• Film Title: Willowmere
Nice to have
• The poster doesn't have to incorporate the photos and can use other design elements like illustrations.
Should not have
• Anything offensive and disturbing.

```html
<!DOCTYPE html>
<html lang="en">
<head>
<meta charset="utf-8">
<title>Willowmere – Film Poster</title>
<link rel="stylesheet" href="https://fonts.googleapis.com/css2?family=Open+Sans:wght@400;600&family=Playfair+Display:wght@800&display=swap">
<style>
  :root {
    --paper-light: #f1f1f0;
    --paper-mid: #dcdcdb;
    --paper-edge: #b9b9b8;
    --credit-ink: #2b2b2b;
  }
  html, body {
    margin: 0;
    padding: 0;
    width: 777px;
    height: 1200px;
    overflow: hidden;
    background: var(--paper-mid);
  }
  .poster {
    position: relative;
    width: 777px;
    height: 1200px;
    overflow: hidden;
    background:
      radial-gradient(ellipse at 50% 40%, var(--paper-light) 0%, var(--paper-mid) 60%, var(--paper-edge) 100%);
  }
  .title-letters {
    position: absolute;
    left: 0;
    top: 0;
    width: 777px;
    height: 1000px;
  }
  .title-letters text {
    font-family: "Playfair Display", serif;
    font-weight: 800;
    font-size: 200px;
    text-anchor: middle;
  }
  .credits {
    position: absolute;
    left: 11px;
    right: 10px;
    top: 1002px;
    margin: 0;
    font-family: "Open Sans", sans-serif;
    font-size: 17.5px;
    line-height: 25px;
    color: var(--credit-ink);
  }
  .credits p { margin: 0; white-space: nowrap; }
</style>
</head>
<body>
<main class="poster">
  <svg class="title-letters" viewBox="0 0 777 1000" role="img"
       aria-label="Film title Willowmere in large letters, each letter filled with film stills: a playground with a mascot, park grass, an older father indoors and a smiling schoolgirl">
    <defs>
      <linearGradient id="still-playground" gradientUnits="userSpaceOnUse" x1="150" y1="50" x2="650" y2="220">
        <stop offset="0" stop-color="#2f6b3a"/>
        <stop offset="0.4" stop-color="#4d8fbd"/>
        <stop offset="0.7" stop-color="#9fb6c6"/>
        <stop offset="1" stop-color="#b6403c"/>
      </linearGradient>
      <linearGradient id="still-mascot" gradientUnits="userSpaceOnUse" x1="150" y1="240" x2="650" y2="400">
        <stop offset="0" stop-color="#e06a22"/>
        <stop offset="0.35" stop-color="#8f8a80"/>
        <stop offset="0.7" stop-color="#a9aea8"/>
        <stop offset="1" stop-color="#6f7c70"/>
      </linearGradient>
      <linearGradient id="still-grass" gradientUnits="userSpaceOnUse" x1="150" y1="430" x2="650" y2="590">
        <stop offset="0" stop-color="#9aa596"/>
        <stop offset="0.45" stop-color="#5a8636"/>
        <stop offset="1" stop-color="#44722a"/>
      </linearGradient>
      <linearGradient id="still-interior" gradientUnits="userSpaceOnUse" x1="150" y1="620" x2="650" y2="780">
        <stop offset="0" stop-color="#b7aea3"/>
        <stop offset="0.4" stop-color="#7d6557"/>
        <stop offset="0.7" stop-color="#c9c3bb"/>
        <stop offset="1" stop-color="#3a3433"/>
      </linearGradient>
      <linearGradient id="still-portrait" gradientUnits="userSpaceOnUse" x1="150" y1="800" x2="650" y2="960">
        <stop offset="0" stop-color="#5e6f7a"/>
        <stop offset="0.35" stop-color="#aeb3b5"/>
        <stop offset="0.7" stop-color="#2f2b2b"/>
        <stop offset="1" stop-color="#cdb9a7"/>
      </linearGradient>
    </defs>
    <g class="row row-1" fill="url(#still-playground)">
      <text x="270" y="200">W</text>
      <text x="530" y="200">I</text>
    </g>
    <g class="row row-2" fill="url(#still-mascot)">
      <text x="270" y="385">L</text>
      <text x="530" y="385">L</text>
    </g>
    <g class="row row-3" fill="url(#still-grass)">
      <text x="270" y="570">O</text>
      <text x="530" y="570">W</text>
    </g>
    <g class="row row-4" fill="url(#still-interior)">
      <text x="270" y="755">M</text>
      <text x="530" y="755">E</text>
    </g>
    <g class="row row-5" fill="url(#still-portrait)">
      <text x="270" y="940">R</text>
      <text x="530" y="940">E</text>
    </g>
  </svg>

  <section class="credits">
    <p>Cast:&nbsp; Noriza Latef, Rashid Tembo Gavin Lu, Delia Rahn, Marisol Teng</p>
    <p>Producer: Darren Voss Co Directors:&nbsp; Hakim Sulong and Celine Moh,Darren Voss</p>
    <p>Director of Photography:&nbsp; Victor Lim&nbsp; Camera Assistant:&nbsp; Ardiman Yusri</p>
    <p>Sound:&nbsp; Rafina Salleh&nbsp; Editor:&nbsp; Peter Alan Corwell&nbsp; Production Designer:&nbsp; Ivy Quek</p>
    <p>Production Art Assistant:&nbsp; Faizal Omar &amp; Bryan Goh</p>
    <p>Music Composer:&nbsp; Wu Ping and Lee Kai Wen Production Assistant:&nbsp; Sofia Rahmat</p>
    <p>Assistant Producer:&nbsp; Tan Mei Ling&nbsp; Production Company:&nbsp; Lumen Reel Pictures</p>
  </section>
</main>
</body>
</html>
```